Funky new Serviced Apartment Company needs a website + logo

Bright Nest Serviced Accommodation is a new company aiming to attract customers who need temporary accommodation (2 days to 6 months) in city locations.

Our customers make considerable savings on longer stays compared to hotels, and have all the creature comforts of home including super-fast WIFI, comfy beds, full kitchen and modern, yet comfortable, furniture.

Another key feature of the design is a page to attract "Partners" who "Work with Us" by allowing us to manage their properties and becoming part of our network of accommodation units. I have include a brochure from one of our competitors, and a video can be found here: http://lnkvault-example.com/aptclip-7 - both can be used as I have permission.

The website design should work on all devices and screen sizes, and lend itself to a mobile app.

We would like to see website designs that are modern and simple, with a strong brand logo. The final design should communicate "Home From Home" and aim to attract professionals away from home on business for long periods of time.

Target Market(s)

Professional People working away from home for extended periods of time

Industry/Entity Type

Accommodation

Contact Information for Business Card

Name, Title, Phone Number, Email
Callum Fenwick, Owner, 07831 552907, callum.fenwick@brightnestsa-example.co.uk

Logo Text

Bright Nest Service Accommodation (Serviced Accommodation optional)

Coding

Coded - Design and coding required

Number of Pages Required

3 page

Font styles to use
Sans Serif

Requirements
Must have
• A 3 page website: Home, Partners, Contact Us
• Home page should have an area to list current apartment units, the user should be able to select a location and filter the list based on price and number of people.
• Partners page should inspire a "Work with us" call to action.
• The design should work with all screen sizes and devices.
• The design should say friendly and professional
Nice to have
• A simple logo, perhaps a smiling face made up using letters 'W' and 'H'.
• A neutral color scheme
Should not have
• No garish or vivid color scheme

```html
<!DOCTYPE html>
<html lang="en">
<head>
<meta charset="utf-8">
<title>Larkfield Serviced Apartments</title>
<link rel="stylesheet" href="https://fonts.googleapis.com/css2?family=Roboto+Condensed:wght@400;700&family=Roboto:wght@300;400;500&family=Alegreya:ital,wght@1,400;1,700&display=swap">
<style>
:root{
  --teal:#2a7a93;
  --teal-dark:#1f6479;
  --ink:#333537;
  --body:#5c5f62;
  --muted:#8a8d90;
  --line:#d6d8da;
  --white:#ffffff;
  --footer:#161718;
  --hero-top:#4c6a86;
  --hero-bottom:#1c2a3b;
}
*{margin:0;padding:0;box-sizing:border-box}
html,body{width:1200px;height:3377px;overflow:hidden;background:var(--white)}
body{position:relative;font-family:"Roboto",Arial,sans-serif;color:var(--ink)}
.abs{position:absolute}
.cond{font-family:"Roboto Condensed",Arial,sans-serif}

/* Hero */
.hero{left:0;top:0;width:1200px;height:630px;background:linear-gradient(180deg,var(--hero-top) 0%,#34506b 45%,var(--hero-bottom) 100%)}
.brand{display:flex;align-items:center;gap:14px;color:var(--white)}
.brand-mark{width:44px;height:44px;border-radius:50%;background:var(--white)}
.brand-name{font-family:"Roboto Condensed",Arial,sans-serif;font-weight:400;color:var(--white);line-height:1.05;font-size:34px;letter-spacing:1px;text-transform:uppercase}
.brand-name small{display:block;font-size:15px;letter-spacing:2px}
.nav{right:150px;top:52px;display:flex;gap:44px;font-size:14px;color:var(--white)}
.nav a{color:var(--white);text-decoration:none;padding-bottom:8px}
.nav a.active{color:#7fc6dc;border-bottom:2px solid #7fc6dc}
.hero-title{left:150px;top:244px;font-family:"Roboto Condensed",Arial,sans-serif;font-weight:700;font-size:56px;line-height:60px;color:var(--white);letter-spacing:1px}
.hero-text{left:150px;top:370px;width:480px;font-size:15px;line-height:22px;color:var(--white)}
.round-btn{width:34px;height:34px;border:2px solid currentColor;border-radius:50%;display:flex;align-items:center;justify-content:center}
.hero-arrows{left:1014px;top:274px;color:var(--white);display:flex;flex-direction:column;gap:12px}

/* Location */
.locator{left:150px;top:574px;width:900px;height:686px;background:var(--white);box-shadow:0 6px 24px rgba(0,0,0,.12)}
.map{left:60px;top:40px;width:800px;height:500px;background:radial-gradient(ellipse at 50% 45%,#dfe6e8 0%,#eef2f3 60%,#fafbfb 100%)}
.locator-title{left:0;top:56px;width:900px;text-align:center;font-family:"Roboto Condensed",Arial,sans-serif;font-weight:700;font-size:54px;letter-spacing:3px;color:var(--ink)}
.units-title{left:14px;top:412px;font-family:"Roboto Condensed",Arial,sans-serif;font-weight:700;font-size:23px;line-height:26px;color:var(--ink)}
.units-list{left:14px;top:474px;list-style:none;font-size:12px;color:var(--body)}
.units-list li{height:24px}
.units-list li::before{content:"–";margin-right:10px;color:var(--muted)}
.select{height:34px;border:1px solid #b9bcbf;font-size:11px;letter-spacing:.5px;color:var(--body);display:flex;align-items:center;justify-content:space-between;padding:0 10px}
.select::after{content:"";border:5px solid transparent;border-top:7px solid var(--ink);border-bottom:0}
.btn{background:var(--teal);color:var(--white);font-family:"Roboto Condensed",Arial,sans-serif;font-weight:700;letter-spacing:1.5px;display:flex;align-items:center;justify-content:center}

/* Welcome */
.photo{background:linear-gradient(135deg,#c9b39a,#8b7b6c)}
.welcome-title{left:675px;top:1418px;font-family:"Roboto Condensed",Arial,sans-serif;font-weight:700;font-size:52px;color:var(--ink);letter-spacing:1px}
.welcome-sub{left:675px;top:1480px;font-family:"Roboto Condensed",Arial,sans-serif;font-size:23px;letter-spacing:2px;color:var(--teal)}
.welcome-text{left:675px;top:1524px;width:380px;font-size:12.5px;line-height:21px;color:var(--body)}
.welcome-text p+p{margin-top:16px}

/* Know you */
.know-title{left:150px;top:1906px;padding-left:22px;border-left:4px solid var(--teal);font-family:"Roboto Condensed",Arial,sans-serif;font-weight:700;font-size:52px;line-height:56px;color:var(--ink)}
.know-text{left:150px;top:2040px;width:900px;font-size:12.5px;line-height:21px;color:var(--ink)}

/* Testimonials */
.testi-title{right:151px;top:2652px;padding-right:14px;border-right:4px solid var(--teal);font-family:"Roboto Condensed",Arial,sans-serif;font-weight:700;font-size:54px;line-height:60px;color:var(--ink);letter-spacing:1px}
.quote{left:240px;top:2740px;width:812px;text-align:right;font-family:"Alegreya",Georgia,serif;font-style:italic;font-size:21px;line-height:31px;color:var(--ink)}
.quote-author{right:150px;top:2832px;text-align:right;font-family:"Alegreya",Georgia,serif;font-style:italic;font-weight:700;font-size:19px;color:var(--teal)}
.quote-place{right:150px;top:2862px;font-family:"Alegreya",Georgia,serif;font-style:italic;font-size:13px;color:var(--ink)}
.testi-arrows{left:150px;top:2768px;color:var(--teal);display:flex;flex-direction:column;gap:10px}

/* Footer */
.footer{left:0;top:2942px;width:1200px;height:389px;background:linear-gradient(180deg,var(--footer),#242628)}
.footer-intro{left:225px;top:3084px;width:350px;font-size:13px;line-height:19px;color:var(--white)}
.contact-row{left:225px;display:flex;gap:14px;font-size:12px;line-height:18px;color:#d9dadb}
.contact-row svg{flex:none;margin-top:2px}
.foot-head{font-family:"Roboto Condensed",Arial,sans-serif;font-weight:700;font-size:16px;letter-spacing:1px;color:var(--white)}
.quick{left:590px;top:3082px;list-style:none;font-size:12px;color:#d9dadb}
.quick li{height:37px}
.quick li::before{content:"›";margin-right:6px}
.field{left:772px;width:270px;background:var(--white);font-size:11px;color:var(--muted);padding:8px 10px;display:flex;justify-content:space-between}
.bottom-bar{left:0;top:3331px;width:1200px;height:46px;background:var(--teal)}
.copyright{left:225px;top:3346px;font-size:12px;color:var(--white)}
.socials{left:912px;top:3340px;display:flex;gap:8px}
.socials span{width:22px;height:22px;border-radius:50%;background:var(--white)}
</style>
</head>
<body>

<!-- Hero -->
<header class="abs hero" role="img" aria-label="Photograph of a dense city skyline of glass towers under a blue sky"></header>
<div class="abs brand" style="left:150px;top:34px">
  <span class="brand-mark"></span>
  <span class="brand-name">Larkfield<small>Serviced Apartments</small></span>
</div>
<nav class="abs nav">
  <a class="active" href="#">Home</a>
  <a href="#">Partners</a>
  <a href="#">Contact Us</a>
</nav>
<h1 class="abs hero-title">YOU’RE IN SAFE<br>HANDS</h1>
<p class="abs hero-text">We understand that everyone’s situation is different. That’s why we take the time to work with you to achieve exactly what you want from your serviced apartment.</p>
<div class="abs hero-arrows">
  <span class="round-btn"><svg width="12" height="14" viewBox="0 0 12 14"><path d="M6 13V2M1 6l5-5 5 5" stroke="currentColor" stroke-width="2" fill="none"/></svg></span>
  <span class="round-btn"><svg width="12" height="14" viewBox="0 0 12 14"><path d="M6 1v11M1 8l5 5 5-5" stroke="currentColor" stroke-width="2" fill="none"/></svg></span>
</div>

<!-- Location selector -->
<section class="abs locator">
  <div class="abs map" role="img" aria-label="Faint world map showing the apartment locations"></div>
  <h2 class="abs locator-title">SELECT LOCATION</h2>
  <svg class="abs" style="left:0;top:0" width="900" height="400" viewBox="0 0 900 400">
    <g fill="none" stroke="#9aa3a8" stroke-width="1.5" stroke-dasharray="3 4">
      <path d="M55 306 Q160 350 190 335 T320 318 T440 300 T540 270 T720 300 T808 312"/>
      <path d="M55 306 V390"/>
    </g>
    <g font-family="Roboto Condensed, Arial, sans-serif" font-weight="700" text-anchor="middle">
      <g transform="translate(55,250)"><path d="M0 52 L-14 30 A29 29 0 1 1 14 30Z" fill="var(--teal)"/><circle r="20" fill="#fff"/><text y="7" font-size="19" fill="#333">01</text></g>
      <g transform="translate(190,282)"><path d="M0 52 L-14 30 A29 29 0 1 1 14 30Z" fill="var(--teal)"/><circle r="20" fill="#fff"/><text y="7" font-size="19" fill="#333">02</text></g>
      <g transform="translate(345,265)"><path d="M0 52 L-14 30 A29 29 0 1 1 14 30Z" fill="var(--teal)"/><circle r="20" fill="#fff"/><text y="7" font-size="19" fill="#333">03</text></g>
      <g transform="translate(471,240)"><path d="M0 52 L-14 30 A29 29 0 1 1 14 30Z" fill="var(--teal)"/><circle r="20" fill="#fff"/><text y="7" font-size="19" fill="#333">04</text></g>
      <g transform="translate(592,196)"><path d="M0 52 L-14 30 A29 29 0 1 1 14 30Z" fill="var(--teal)"/><circle r="20" fill="#fff"/><text y="7" font-size="19" fill="#333">05</text></g>
      <g transform="translate(712,268)"><path d="M0 28 L-8 17 A16 16 0 1 1 8 17Z" fill="var(--teal)"/><circle r="11" fill="#fff"/><text y="4" font-size="10" fill="#333">06</text></g>
      <g transform="translate(808,292)"><path d="M0 28 L-8 17 A16 16 0 1 1 8 17Z" fill="var(--teal)"/><circle r="11" fill="#fff"/><text y="4" font-size="10" fill="#333">07</text></g>
    </g>
  </svg>
  <h3 class="abs units-title">CURRENT APARTMENT<br>UNITS</h3>
  <ul class="abs units-list">
    <li>Lorem ipsum</li><li>Iconsectetur</li><li>Aliquam tortor orci</li><li>Fermentum pharetra</li><li>Esed augue ma</li><li>Aquam nec</li><li>Pcursus quis</li>
  </ul>
  <div class="abs select" style="left:291px;top:538px;width:249px">Based on Price</div>
  <div class="abs select" style="left:552px;top:538px;width:257px">Number of People</div>
  <div class="abs btn" style="left:464px;top:590px;width:102px;height:36px;font-size:17px">SUBMIT</div>
  <svg class="abs" style="left:580px;top:601px" width="62" height="14" viewBox="0 0 62 14"><path d="M62 7H3M9 1L2 7l7 6" stroke="#333" stroke-width="1.6" fill="none"/></svg>
</section>

<!-- Welcome -->
<div class="abs photo" style="left:0;top:1333px;width:410px;height:506px;background:linear-gradient(140deg,#d8c8b2,#b8a58e 50%,#8a7563)" role="img" aria-label="Photograph of a bright living room with a white sofa and warm lamps"></div>
<div class="abs photo" style="left:410px;top:1333px;width:232px;height:169px;background:linear-gradient(160deg,#8d8f93,#3b3d42)" role="img" aria-label="Photograph of a made double bed in a modern bedroom"></div>
<div class="abs photo" style="left:410px;top:1502px;width:232px;height:169px;background:linear-gradient(160deg,#b88a5c,#6e4a2e)" role="img" aria-label="Photograph of an open-plan kitchen and dining area"></div>
<div class="abs photo" style="left:410px;top:1671px;width:232px;height:168px;background:linear-gradient(160deg,#2b3a86,#141c4a)" role="img" aria-label="Photograph of a bedroom with a deep blue feature wall"></div>
<h2 class="abs welcome-title">WELCOME TO</h2>
<p class="abs welcome-sub">LARKFIELD SERVICED APARTMENTS</p>
<div class="abs welcome-text">
  <p>We founded Larkfield Serviced Apartments as property owners and investors ourselves, who were unable to source a managing agent specialising in the operations of Serviced Accommodation – indeed we still operate our own properties via Larkfield – we decided that since no one would run our Serviced Apartments as we wanted, then we’d just have to do it ourselves!</p>
  <p>We now offer a wide range of accommodation to meet our guest’s needs and budget, with discounts available for longer stays. We have formed global partnerships with major corporates, and we pass on the benefits of these alliances to our Landlords, in order that you may maximise your returns, with a minimum of hassle. We are on hand to answer your questions, offer advice or provide support at any time, if you would like to talk to someone, our friendly team are ready and waiting to chat to you on 01632 960 418.</p>
</div>

<!-- Know you -->
<h2 class="abs know-title">WE’D LOVE TO GET TO<br>KNOW YOU BETTER</h2>
<p class="abs know-text">Whichever stage you’re at, you can trust us to help ease the hassle of operating serviced accommodation. We’ll get to know you and your property, to work out exactly what you’ll need to get the most out of investing and operating in serviced accommodation.</p>

<div class="abs photo" style="left:0;top:2114px;width:374px;height:214px;background:linear-gradient(150deg,#b5a48f,#6d5a48)" role="img" aria-label="Photograph of a table set with flowers and a cake"></div>
<div class="abs photo" style="left:374px;top:2114px;width:225px;height:214px;background:linear-gradient(150deg,#d8b690,#a32a24)" role="img" aria-label="Photograph of a bed with a red throw and folded towels"></div>
<div class="abs photo" style="left:599px;top:2114px;width:234px;height:214px;background:linear-gradient(150deg,#d8c2a4,#8c6c4e)" role="img" aria-label="Photograph of a fitted kitchen with wooden worktops"></div>
<div class="abs photo" style="left:833px;top:2114px;width:367px;height:214px;background:linear-gradient(150deg,#efe0c6,#b89266)" role="img" aria-label="Photograph of a clean bathroom with basin and toilet"></div>
<div class="abs photo" style="left:0;top:2328px;width:599px;height:261px;background:linear-gradient(150deg,#e4e2de,#8a8580)" role="img" aria-label="Photograph of a bedroom with grey cushions and framed prints"></div>
<div class="abs photo" style="left:599px;top:2328px;width:601px;height:261px;background:linear-gradient(150deg,#f0cf9a,#c98a4a 60%,#8f3a2a)" role="img" aria-label="Photograph of a dining table laid with glasses and red roses"></div>

<!-- Testimonials -->
<h2 class="abs testi-title">CLIENTS TESTIMONIALS</h2>
<p class="abs quote">Excellent communication via email, phone &amp; text, key box entry very convenient. Building and flat very clean, bedding &amp; furnishings very good condition, felt brand new.</p>
<p class="abs quote-author">Guest Review, Ashgrove House,</p>
<p class="abs quote-place">Kelvinford</p>
<div class="abs testi-arrows">
  <span class="round-btn"><svg width="12" height="14" viewBox="0 0 12 14"><path d="M6 13V2M1 6l5-5 5 5" stroke="currentColor" stroke-width="2" fill="none"/></svg></span>
  <span class="round-btn"><svg width="12" height="14" viewBox="0 0 12 14"><path d="M6 1v11M1 8l5 5 5-5" stroke="currentColor" stroke-width="2" fill="none"/></svg></span>
</div>

<!-- Footer -->
<footer class="abs footer" role="img" aria-label="Dark photograph of a city at night behind the footer"></footer>
<div class="abs brand" style="left:150px;top:3010px">
  <span class="brand-mark"></span>
  <span class="brand-name">Larkfield<small>Serviced Apartments</small></span>
</div>
<p class="abs footer-intro">Contact our serviced accommodation portfolio team to experience the Larkfield service.</p>
<div class="abs contact-row" style="top:3146px"><svg width="12" height="10" viewBox="0 0 12 10"><rect x=".5" y=".5" width="11" height="9" fill="none" stroke="#fff"/><path d="M.5 .5l5.5 5 5.5-5" fill="none" stroke="#fff"/></svg>office@larkfield-example.co.uk</div>
<div class="abs contact-row" style="top:3182px"><svg width="12" height="12" viewBox="0 0 12 12"><path d="M3 0l2 3-1.5 1.5a7 7 0 003.5 3.5L8.5 6.5l3 2-1.5 3C5 11 1 7 .5 2z" fill="#fff"/></svg>+44 1632 960 418</div>
<div class="abs contact-row" style="top:3218px"><svg width="10" height="14" viewBox="0 0 10 14"><path d="M5 14S0 8 0 5a5 5 0 0110 0c0 3-5 9-5 9z" fill="#fff"/><circle cx="5" cy="5" r="2" fill="#1a1b1c"/></svg>Larkfield Serviced Apartments, 4-6 Mercer Row,<br>Halbridge, England, HB2 7QT, UK</div>

<h4 class="abs foot-head" style="left:590px;top:3046px">QUICK LINK</h4>
<ul class="abs quick"><li>Home</li><li>Partners</li><li>Contact Us</li></ul>

<h4 class="abs foot-head" style="left:772px;top:3046px">GET IN TOUCH</h4>
<div class="abs field" style="top:3086px;height:32px">Name <svg width="10" height="12" viewBox="0 0 10 12"><circle cx="5" cy="3" r="3" fill="#333"/><path d="M0 12a5 5 0 0110 0z" fill="#333"/></svg></div>
<div class="abs field" style="top:3124px;height:30px">Email <svg width="10" height="10" viewBox="0 0 10 10"><rect y="3" width="10" height="7" fill="#333"/><path d="M2.5 3V2a2.5 2.5 0 015 0v1" stroke="#333" fill="none"/></svg></div>
<div class="abs field" style="top:3162px;height:72px">Comments</div>
<div class="abs btn" style="left:772px;top:3246px;width:83px;height:30px;font-size:15px">SEND</div>
<svg class="abs" style="left:872px;top:3254px" width="62" height="14" viewBox="0 0 62 14"><path d="M62 7H3M9 1L2 7l7 6" stroke="#fff" stroke-width="1.6" fill="none"/></svg>

<div class="abs bottom-bar"></div>
<p class="abs copyright">© 2017 Larkfield Serviced Apartments. All rights reserved.</p>
<div class="abs socials"><span></span><span></span><span></span><span></span><span></span><span></span></div>

</body>
</html>
```